Brochure - Capabilities Statement doc - 1 page handout

I would like to upgrade our "capabilities statement" brochure doc to look more professional and designed with a tailored modern look. see attached document for details. We use this document when we are in meetings or when we introduce our company in an email to a new prospect client. Its a one page overview of the services we provide. At the moment it is a terrible juvenile looking doc. with no thought to design. I am hoping you can change that and help capture our customers attention when they read it.

Target Market(s)

Our client base is corporations, tech companies and non-profits

Industry/Entity Type

It Professional

Font styles to use
Sans Serif

Requirements
Must have
• I'd like a cleaver sharp look to it. Not just columns and bullet points like I have now. This will be emailed to clients in a pdf and I'd like to have a hand out when in meetings.

```html
<!DOCTYPE html>
<html lang="en">
<head>
<meta charset="utf-8">
<title>Summit Link – Capabilities Statement</title>
<link href="https://fonts.googleapis.com/css2?family=Montserrat:wght@600;700&family=Questrial&display=swap" rel="stylesheet">
<style>
  :root {
    --orange: #ee8a2b;
    --orange-deep: #e2741c;
    --grey: #cfcfcf;
    --text: #5a5a5a;
    --white: #ffffff;
    --page-bg: #f2f2f2;
    --badge-blue: #1f4f8a;
    --badge-sage: #d9e3cf;
  }
  * { box-sizing: border-box; margin: 0; padding: 0; }
  html, body { width: 993px; height: 1200px; overflow: hidden; background: var(--page-bg); }
  body { font-family: "Questrial", "Century Gothic", sans-serif; color: var(--text); }

  .sheet { position: relative; width: 993px; height: 1200px; background: var(--white); overflow: hidden; }

  .hero-photo {
    position: absolute; left: 0; top: 0; width: 993px; height: 380px;
    background: linear-gradient(120deg, #7a3414 0%, #b4561f 35%, #d98a45 60%, #8c4a22 100%);
  }
  .shapes { position: absolute; left: 0; top: 0; }

  .brand {
    position: absolute; left: 230px; top: 90px;
    display: flex; align-items: center; gap: 16px;
  }
  .brand-dot { width: 96px; height: 96px; border-radius: 50%; background: var(--orange); }
  .brand-name { font-family: "Montserrat", sans-serif; font-weight: 700; font-size: 26px; color: var(--white); letter-spacing: 1px; }

  .collage {
    position: absolute; left: 610px; top: 36px; width: 300px; height: 290px;
    display: grid; grid-template-columns: 1fr 1fr; grid-template-rows: 1fr 1fr; gap: 8px;
    padding: 8px; background: var(--white);
  }
  .collage-tile:nth-child(1) { background: linear-gradient(135deg, #3f3a3c, #8a6d5a); }
  .collage-tile:nth-child(2) { background: linear-gradient(135deg, #e9e4dc, #b59b7f); }
  .collage-tile:nth-child(3) { background: linear-gradient(135deg, #4b4548, #a4683b); }
  .collage-tile:nth-child(4) { background: linear-gradient(135deg, #c9925a, #6e4324); }

  .title-box {
    position: absolute; left: 0; top: 300px; width: 330px; height: 92px;
    background: var(--white); padding: 14px 0 0 44px;
  }
  .title {
    font-family: "Montserrat", sans-serif; font-weight: 700; font-size: 28px; line-height: 32px;
    color: var(--orange); letter-spacing: 1px; text-transform: uppercase;
  }

  .intro {
    position: absolute; left: 44px; top: 410px; width: 520px;
    color: var(--white); font-size: 14px; line-height: 19px;
  }
  .intro p + p { margin-top: 12px; }

  .section-heading {
    font-family: "Montserrat", sans-serif; font-weight: 700; font-size: 17px;
    color: var(--orange); text-transform: uppercase; letter-spacing: 0.5px; margin-bottom: 8px;
  }
  .checklist { list-style: none; }
  .checklist li {
    position: relative; padding-left: 26px; font-size: 14px; line-height: 17px; margin-bottom: 4px;
  }
  .checklist li::before {
    content: ""; position: absolute; left: 0; top: 1px; width: 13px; height: 13px;
    border: 1.5px solid var(--orange);
  }
  .checklist li::after {
    content: ""; position: absolute; left: 4px; top: 1px; width: 5px; height: 9px;
    border: solid var(--orange); border-width: 0 2px 2px 0; transform: rotate(40deg);
  }

  .capabilities { position: absolute; left: 44px; top: 628px; width: 540px; }
  .highlights { position: absolute; left: 44px; top: 950px; width: 540px; }
  .highlights .checklist li { font-size: 15px; }

  .side { position: absolute; left: 630px; top: 395px; width: 330px; }
  .side .checklist li { font-size: 13px; }
  .side-block + .side-block { margin-top: 22px; }
  .codes { font-size: 14px; color: var(--text); }

  .cert-tab {
    position: absolute; left: 0; top: 1128px; height: 40px; padding: 0 46px 0 44px;
    background: var(--orange); color: var(--white);
    font-family: "Montserrat", sans-serif; font-weight: 700; font-size: 14px; letter-spacing: 1px;
    display: flex; align-items: center; text-transform: uppercase;
    clip-path: polygon(0 0, 92% 0, 100% 50%, 92% 100%, 0 100%);
  }
  .cert-badges { position: absolute; right: 40px; top: 1115px; display: flex; align-items: center; gap: 26px; }
  .badge { width: 56px; height: 56px; background: var(--grey); }
  .badge-round { border-radius: 50%; }
  .badge-blue { background: var(--badge-blue); }
  .badge-sage { background: var(--badge-sage); }
  .badge-divider { width: 1px; height: 50px; background: var(--grey); }

  .footer-stripe { position: absolute; left: 0; bottom: 0; width: 993px; height: 12px; background: var(--orange); }
</style>
</head>
<body>
<main class="sheet">
  <div class="hero-photo" role="img" aria-label="Warm toned photo of a banquet hall set for an event"></div>

  <svg class="shapes" width="993" height="1200" viewBox="0 0 993 1200" aria-hidden="true">
    <polygon points="570,400 993,210 993,1200 570,1200" fill="#ffffff"/>
    <polygon points="0,640 600,570 600,1200 0,1200" fill="#ffffff"/>
    <polygon points="0,282 380,262 380,300 0,300" fill="#cfcfcf"/>
    <polygon points="0,360 600,300 600,570 0,640" fill="#ee8a2b"/>
    <polygon points="330,330 600,300 600,330" fill="#e2741c"/>
  </svg>

  <div class="brand">
    <span class="brand-dot"></span>
    <span class="brand-name">SUMMIT LINK</span>
  </div>

  <div class="collage">
    <div class="collage-tile" role="img" aria-label="Photo of guests at a conference dinner"></div>
    <div class="collage-tile" role="img" aria-label="Photo of a plated catering buffet"></div>
    <div class="collage-tile" role="img" aria-label="Photo of an event reception crowd"></div>
    <div class="collage-tile" role="img" aria-label="Photo of pastries on a serving table"></div>
  </div>

  <div class="title-box">
    <h1 class="title">Capabilities<br>Statement</h1>
  </div>

  <div class="intro">
    <p>Summit Link is a meeting, event and project management services company. We specialize in capturing your ideas, objectives and budget and transforming them into an unforgettable experience.</p>
    <p>Summit Link has been in business for over 18 years and has amassed over 130 years of combined staff experience. Our expertise includes customized online registration software, destination selection as well as housing and onsite management. Our ability to leverage our buying power and excellent reputation ensures that our clients procure the best value and service for their investment. Summit Link successfully executes over 150 events annually.</p>
  </div>

  <section class="capabilities">
    <h2 class="section-heading">Capabilities</h2>
    <ul class="checklist">
      <li>Site Research and Hotel &amp; Venue Contract Negotiations</li>
      <li>Customized Registration Software &amp; Management</li>
      <li>Citywide Housing Management</li>
      <li>Destination Management Services</li>
      <li>Group Transportation Services</li>
      <li>Airport Meet &amp; Greet Services</li>
      <li>Project Management</li>
      <li>Meeting Management</li>
      <li>Event Management</li>
      <li>Special Event Coordination</li>
      <li>Custom Tours and Activities</li>
      <li>Showroom Installation Services</li>
      <li>Onsite Staff Services / Registration Desk Services &amp; Software</li>
    </ul>
  </section>

  <section class="highlights">
    <h2 class="section-heading">Highlights</h2>
    <ul class="checklist">
      <li>There is no request too large or too small</li>
      <li>Tested and approved suppliers and vendor partnerships</li>
      <li>A-la-carte proposals and services</li>
      <li>Creative experienced team</li>
      <li>We guarantee our work</li>
      <li>We pre-quote the job and honor the quote!</li>
    </ul>
  </section>

  <aside class="side">
    <section class="side-block">
      <h2 class="section-heading">What makes us different?</h2>
      <ul class="checklist">
        <li>Accredited Event Planners (AEP)</li>
        <li>WEGA Certified</li>
        <li>Local, National and International services</li>
        <li>Long-standing client retention through successful partnerships</li>
      </ul>
    </section>
    <section class="side-block">
      <h2 class="section-heading">Our partners:</h2>
      <ul class="checklist">
        <li>Fortune 500 Companies</li>
        <li>Consumer Packaged Goods Industry</li>
        <li>Manufacturing</li>
        <li>Organizations</li>
        <li>Technology Industry</li>
        <li>Non-profit Organizations</li>
        <li>Colleges and Universities</li>
        <li>Client references upon request</li>
      </ul>
    </section>
    <section class="side-block">
      <h2 class="section-heading">NAICS Codes:</h2>
      <p class="codes">561599 &nbsp;|&nbsp; 561920</p>
    </section>
    <section class="side-block">
      <h2 class="section-heading">UNSPSC Codes:</h2>
      <p class="codes">80141607</p>
    </section>
  </aside>

  <div class="cert-tab">Certifications and Associations</div>
  <div class="cert-badges">
    <span class="badge badge-round badge-blue"></span>
    <span class="badge-divider"></span>
    <span class="badge badge-sage"></span>
    <span class="badge-divider"></span>
    <span class="badge badge-round"></span>
  </div>

  <div class="footer-stripe"></div>
</main>
</body>
</html>
```